Letterhead and Envelopes design using existing logo. Logo can be found at tqvanholt.com

Use existing logo (attached) and incorporate in letterhead and envelope designs.

Current logo can be viewed at tqvanholt.com the web site reflect various parent and sub companies. Please see attached as well.

Target Market(s)

Other oil and gas operators.

Industry/Entity Type

Oil And Gas

Font styles to use
Sans Serif

Colors

Designer to choose colors to be used in the design.

Requirements
Must have
• Current logo and address
Nice to have
• Modern, contemporary approach yet incorporate existing traditional design.
• After design is selected for Wexford Tiller Holdings I will use similar design for Royalties, Exploration, Energy and Farms with different color schemes.

```html
<!DOCTYPE html>
<html lang="en">
<head>
<meta charset="utf-8">
<title>Wexford Tiller Holdings — Letterhead</title>
<link href="https://fonts.googleapis.com/css2?family=Open+Sans:wght@400;600&display=swap" rel="stylesheet">
<style>
  :root {
    --backdrop: #e6e6e6;
    --paper: #ffffff;
    --ink: #111111;
    --band: #252525;
    --band-text: #ffffff;
    --accent: #6a9a3f;
  }
  * { box-sizing: border-box; margin: 0; padding: 0; }
  html, body {
    width: 1200px; height: 1200px; overflow: hidden;
    background: var(--backdrop);
    font-family: "Open Sans", sans-serif;
  }
  .letterhead {
    position: absolute;
    left: 168px; top: 20px;
    width: 864px; height: 1160px;
    background: var(--paper);
  }
  .brand {
    position: absolute;
    left: 56px; top: 96px;
    display: flex; align-items: center; gap: 12px;
  }
  .brand-dot {
    width: 40px; height: 40px; border-radius: 50%;
    background: var(--accent);
    flex: none;
  }
  .brand-name {
    font-size: 19px; font-weight: 600; color: var(--ink);
    line-height: 1.15; width: 130px;
  }
  .footer-band {
    position: absolute;
    left: 0; bottom: 0;
    width: 100%; height: 73px;
    background: var(--band);
    color: var(--band-text);
    font-size: 13.5px; line-height: 17px;
  }
  .footer-address {
    position: absolute; left: 56px; top: 12px;
  }
  .footer-address .company { font-weight: 600; }
  .footer-divider {
    position: absolute; left: 281px; top: 14px;
    width: 1px; height: 46px; background: var(--band-text);
  }
  .footer-contact {
    position: absolute; left: 302px; top: 12px;
    list-style: none;
  }
  .footer-contact li { display: flex; align-items: center; gap: 6px; }
  .footer-contact svg { width: 11px; height: 11px; flex: none; }
</style>
</head>
<body>
  <main class="letterhead">
    <div class="brand">
      <span class="brand-dot"></span>
      <span class="brand-name">Wexford Tiller Holdings</span>
    </div>

    <footer class="footer-band">
      <address class="footer-address" style="font-style:normal">
        <div class="company">Wexford Tiller Holdings, LLC.</div>
        <div>PO Box 318 Larkfield,</div>
        <div>Northvale 40219</div>
      </address>
      <span class="footer-divider"></span>
      <ul class="footer-contact">
        <li>
          <svg viewBox="0 0 12 12" aria-hidden="true"><path fill="var(--accent)" d="M2.2 0.8l2 2-1 1.4c.7 1.6 2 2.9 3.6 3.6l1.4-1 2 2-1.2 1.6C5 10.2 1.8 7 1.6 1.9z"/></svg>
          <span>(555) 014.2276</span>
        </li>
        <li>
          <svg viewBox="0 0 12 12" aria-hidden="true"><rect x="1" y="2.5" width="10" height="7" fill="var(--accent)"/><path d="M1 2.5l5 4 5-4" fill="none" stroke="var(--band)" stroke-width="1"/></svg>
          <span>reception@tqvanholt.com</span>
        </li>
        <li>
          <svg viewBox="0 0 12 12" aria-hidden="true"><g fill="none" stroke="var(--accent)" stroke-width="1"><circle cx="6" cy="6" r="4.8"/><ellipse cx="6" cy="6" rx="2" ry="4.8"/><path d="M1.2 6h9.6"/></g></svg>
          <span>www.tqvanholt.com</span>
        </li>
      </ul>
    </footer>
  </main>
</body>
</html>
```